Business Card Design Project

I need a business card for a Management Consultancy. We work with organisational design and development and strategic change using facilitation, consulting and coaching.

Size of card is 90 x 55mm.

Logo is attached.

Wording is:

Carla Brennick
Director

tel 0417286194
email is: info@bluepathvista.com.au

Target Market(s)

Government departments and not for profit organisations mainly.

Industry/Entity Type

Business

Requirements
Must have
• White or colour background not black.

On one side of the card, either back or front please include the words:

Leading Strategic Change

Two sided business card

```html
<!DOCTYPE html>
<html lang="en">
<head>
<meta charset="utf-8">
<title>BluePath Vista Consulting – Business Card</title>
<link rel="stylesheet" href="https://fonts.googleapis.com/css2?family=Arimo:wght@400;700&family=Open+Sans:wght@400;600&display=swap">
<style>
  :root {
    --stage: #3b3e44;
    --card: #f7f7f8;
    --card-shade: #e4e5e8;
    --slate: #4b5263;
    --slate-dark: #3a4050;
    --slate-light: #8a92a3;
    --green: #6cbf2a;
    --ink: #3c3f46;
    --rule: #b9bcc2;
    --band-text: #e9ebef;
    --accent-blue: #3e9cc4;
  }
  * { box-sizing: border-box; margin: 0; padding: 0; }
  html, body {
    width: 1200px; height: 900px; overflow: hidden;
    background: var(--stage);
  }
  .canvas { position: relative; width: 1200px; height: 900px; }

  .card {
    position: absolute; left: 300px;
    width: 600px; height: 367px;
    border-radius: 28px; overflow: hidden;
    background: linear-gradient(160deg, #ffffff 0%, var(--card) 55%, var(--card-shade) 100%);
    box-shadow: 0 10px 26px rgba(0,0,0,0.35);
  }
  .card--back { top: 48px; }
  .card--front { top: 470px; }

  /* Back side */
  .brand-stack {
    position: absolute; left: 0; right: 0; top: 70px;
    display: flex; flex-direction: column; align-items: center; gap: 18px;
  }
  .brand-dot {
    width: 70px; height: 70px; border-radius: 50%;
    background: var(--slate-light);
  }
  .brand-name {
    font-family: "Arimo", Arial, sans-serif; font-weight: 700;
    font-size: 34px; color: var(--slate); letter-spacing: -0.5px;
  }
  .brand-sub {
    font-family: "Arimo", Arial, sans-serif; font-weight: 700;
    font-size: 34px; color: var(--slate); margin-top: -14px;
  }
  .tagline-band {
    position: absolute; left: 0; right: 0; bottom: 70px; height: 34px;
    background: linear-gradient(90deg, rgba(75,82,99,0) 0%, var(--slate) 22%, var(--slate-dark) 100%);
  }
  .tagline {
    position: absolute; left: 0; right: 0; bottom: 70px; height: 34px;
    line-height: 34px; text-align: center;
    font-family: "Open Sans", Arial, sans-serif; font-size: 18px;
    letter-spacing: 1.5px; color: var(--band-text);
  }

  /* Front side */
  .front-brand {
    position: absolute; left: 38px; top: 30px;
    display: flex; align-items: center; gap: 12px;
  }
  .front-brand .brand-dot { width: 50px; height: 50px; }
  .front-brand .brand-name { font-size: 22px; }

  .marker {
    position: absolute; left: 0; top: 104px;
    width: 0; height: 0;
    border-top: 13px solid transparent;
    border-bottom: 13px solid transparent;
    border-left: 16px solid var(--green);
  }
  .person { position: absolute; left: 62px; top: 102px; }
  .person-name {
    font-family: "Arimo", Arial, sans-serif; font-size: 27px; color: var(--ink);
  }
  .person-name .surname { color: var(--green); }
  .person-role {
    font-family: "Arimo", Arial, sans-serif; font-size: 14px; color: var(--ink);
    margin-top: 4px;
  }
  .divider {
    position: absolute; left: 62px; top: 180px; width: 300px; height: 1px;
    background: var(--rule);
  }
  .contact {
    position: absolute; left: 62px; top: 198px;
    font-family: "Open Sans", Arial, sans-serif; font-size: 15px; color: var(--ink);
    line-height: 28px;
  }
  .contact-label { color: var(--green); font-weight: 600; margin-right: 6px; }

  .decor-circle { position: absolute; right: 0; top: 0; }
</style>
</head>
<body>
<main class="canvas">

  <section class="card card--back" aria-label="Card back">
    <div class="brand-stack">
      <div class="brand-dot"></div>
      <div class="brand-name">BluePath Vista</div>
      <div class="brand-sub">Consulting</div>
    </div>
    <div class="tagline-band"></div>
    <p class="tagline">Leading Strategic Change</p>
  </section>

  <section class="card card--front" aria-label="Card front">
    <div class="front-brand">
      <div class="brand-dot"></div>
      <div class="brand-name">BluePath Vista Consulting</div>
    </div>

    <div class="marker"></div>
    <div class="person">
      <h1 class="person-name">Carla <span class="surname">Brennick</span></h1>
      <p class="person-role">Director</p>
    </div>
    <div class="divider"></div>
    <p class="contact">
      <span class="contact-label">t :</span>0417286194<br>
      <span class="contact-label">e :</span>info@bluepathvista.com.au
    </p>

    <svg class="decor-circle" width="600" height="367" viewBox="0 0 600 367" role="img" aria-label="Large brand circle decoration">
      <defs>
        <radialGradient id="decorFill" cx="0.75" cy="0.7" r="0.8">
          <stop offset="0" stop-color="var(--accent-blue)"/>
          <stop offset="0.45" stop-color="#7f8ea6"/>
          <stop offset="1" stop-color="var(--slate)"/>
        </radialGradient>
      </defs>
      <circle cx="640" cy="300" r="225" fill="url(#decorFill)"/>
    </svg>
  </section>

</main>
</body>
</html>
```